Surgical Procedure Room Letterhead

PLEASE DO NOT MAKE YOUR LETTERHEAD SIMILAR TO THE ONE I AM INCLUDING IN MY UPLOADS

Hello! I need my logo used to make a very clean, professional, simple letterhead that has all the pertinent information in it:
Location: 4182 NW 38th Lane, Suite 500
Tamarac, FL 33967
Phone: 954-218-4650
Fax: 800-642-9082

Can you please put this all on a word document that is easily editable? I will include my practice letterhead as an example ONLY of how easy it should be to write below the letterhead. Please don't make this letterhead the same as the one I am including in this example. They are two separate businesses.

Target Market(s)

Insurance companies

Industry/Entity Type

medical

Requirements
Must have
• classiness, elegance, simplicity
Should not have
• Please don't make your letterhead the same as the one that I included in my uploads

```html
<!DOCTYPE html>
<html lang="en">
<head>
<meta charset="utf-8">
<title>Surgiview Suites Letterhead</title>
<link href="https://fonts.googleapis.com/css2?family=Montserrat:wght@400;500;600&display=swap" rel="stylesheet">
<style>
  :root {
    --bg: #ececec;
    --paper: #ffffff;
    --navy: #1f3d66;
    --gold: #d4b04c;
    --ink: #3a3f4a;
    --sign: #2436a8;
  }
  html, body { margin: 0; padding: 0; overflow: hidden; }
  body {
    width: 1200px; height: 900px;
    background: var(--bg);
    font-family: "Montserrat", sans-serif;
    position: relative;
  }
  .letterhead {
    position: absolute; left: 300px; top: 26px;
    width: 600px; height: 848px;
    background: var(--paper);
    box-shadow: 0 4px 18px rgba(0,0,0,.12);
    overflow: hidden;
  }
  .brand {
    position: absolute; left: 56px; top: 120px;
    display: flex; align-items: center; gap: 10px;
  }
  .brand-dot { width: 22px; height: 22px; border-radius: 50%; background: var(--gold); }
  .brand-name {
    font-weight: 600; font-size: 19px; letter-spacing: 1.5px;
    color: var(--navy); margin: 0;
  }
  .letter-body {
    position: absolute; left: 56px; top: 262px; width: 440px;
    font-size: 9px; line-height: 1.45; color: var(--ink);
  }
  .letter-body p { margin: 0 0 12px; }
  .signoff { position: absolute; left: 190px; top: 566px; }
  .signature {
    width: 120px; height: 26px;
    background: linear-gradient(90deg, rgba(36,54,168,.15), rgba(36,54,168,.05));
    border-radius: 3px;
  }
  .signoff-role { font-size: 9px; color: var(--ink); margin: 4px 0 0; }
  .footer {
    position: absolute; left: 0; right: 0; bottom: 36px;
    display: flex; align-items: stretch;
    font-size: 9.5px; color: var(--navy); line-height: 1.5;
  }
  .footer-address { width: 322px; text-align: right; padding-right: 12px; font-style: normal; }
  .footer-divider { width: 1px; background: var(--gold); }
  .footer-contact { padding-left: 12px; }
  .footer-contact p, .footer-address p { margin: 0; }
  .band-navy { position: absolute; left: 0; bottom: 0; width: 334px; height: 7px; background: var(--navy); }
  .band-gold { position: absolute; left: 334px; right: 0; bottom: 0; height: 22px; background: var(--gold); }
</style>
</head>
<body>
  <main class="letterhead">
    <header class="brand">
      <span class="brand-dot"></span>
      <h1 class="brand-name">SURGIVIEW SUITES</h1>
    </header>

    <section class="letter-body">
      <p>Letterhead samples are a great way of deciding what kind of letterhead you want to design for you and your company. The internet has a ton of great letterhead samples to browse through. Whether you want something simple, with just a couple lines of text of your business information, or something decorative and stunning, with photos and logos on the top and bottom of the page, it will be easy to find what you want, because there are samples online for basically any type of letterhead you could want.</p>
      <p>Any business could easily benefit from browsing through some letterhead samples, if only to get an idea for what kind of letterhead their company might want. Letterheads are just one of the tools that a business professional could use to help increase their customer base, and to really be memorable to everyone they write a letter to. Letterhead is quite an effective tool for marketing and advertising, but because it's such a simple and well known idea, it is often unfairly overlooked. Make sure you don't make that mistake, and make some letterhead samples of your own today.</p>
      <p>Whether you want to get new customers to remember you and become part of your clientele, or you just want to send out friendly reminders to your existing clients, customizing your own letterhead samples can really help you out. Try out some letterhead samples and you will not regret it, and I'm sure you will add a new tool to your business' arsenal of networking, marketing, and advertising tools.</p>
    </section>

    <div class="signoff">
      <div class="signature" role="img" aria-label="Handwritten signature of Daniel Hartwell"></div>
      <p class="signoff-role">company director</p>
    </div>

    <footer class="footer">
      <address class="footer-address">
        <p>4182 NW 38th Lane, Suite 500</p>
        <p>Tamarac, FL 33967</p>
      </address>
      <span class="footer-divider"></span>
      <div class="footer-contact">
        <p>Phone: 954-218-4650</p>
        <p>Fax: 800-642-9082</p>
      </div>
    </footer>

    <div class="band-navy"></div>
    <div class="band-gold"></div>
  </main>
</body>
</html>
```